Business card for law firm

Need business card for new law firm. Think confident, authoritative, conservative, but not stuffy or old-fashioned.

Contact Information for Business Card

Content for card - logo (uploaded), plus the following:

Paul Wexbury (larger font)
Managing Partner (larger font, but not as large as name)
Level 9, 41 Tansy Lane
Sydney NSW 2000
Main Tel 02 7346 2190
Direct Tel 02 6273 4415
Email paul@qvlegal.com.au
www.qvlegal.com.au

Letterhead design should include logo plus:
Level 9, 41 Tansy Lane
Sydney NSW 2000
Tel 02 6273 4415
www.qvlegal.com.au

```html
<!DOCTYPE html>
<html lang="en">
<head>
<meta charset="utf-8">
<title>Quillvane Lawyers – Business Card</title>
<link rel="stylesheet" href="https://fonts.googleapis.com/css2?family=Cinzel:wght@400&family=Lato:wght@400;700&display=swap">
<style>
  :root {
    --backdrop: #2b2b2c;
    --card-dark: #111112;
    --card-dark-ink: #4a4a4e;
    --accent-soft: #7f94c8;
    --card-light: #ffffff;
    --navy: #1f2466;
    --ink: #1a1a1a;
    --ghost: #e0e0e0;
  }
  * { margin: 0; padding: 0; box-sizing: border-box; }
  html, body { width: 1200px; height: 716px; overflow: hidden; }
  body { background: var(--backdrop); position: relative; font-family: 'Lato', sans-serif; }

  .card {
    position: absolute;
    top: 208px;
    width: 520px;
    height: 300px;
    border-radius: 18px;
    overflow: hidden;
  }

  /* Front */
  .card-front { left: 50px; background: var(--card-dark); }
  .front-brand {
    position: absolute; left: 0; right: 0; top: 90px;
    display: flex; flex-direction: column; align-items: center; gap: 22px;
  }
  .front-brand .brand-square { width: 48px; height: 48px; background: var(--accent-soft); }
  .front-brand .brand-name {
    font-family: 'Lato', sans-serif; font-weight: 400;
    font-size: 30px; line-height: 1; color: var(--card-dark-ink);
  }

  /* Back */
  .card-back { left: 630px; background: var(--card-light); }
  .back-brand {
    position: absolute; left: 14px; top: 0; height: 300px;
    writing-mode: vertical-rl; transform: rotate(180deg);
    text-align: center; font-family: 'Lato', sans-serif; font-weight: 400;
    font-size: 30px; line-height: 1; color: var(--ghost);
  }

  .person { position: absolute; left: 120px; top: 40px; }
  .person-name { font-family: 'Cinzel', serif; font-weight: 400; font-size: 25px; color: var(--ink); letter-spacing: 0.5px; }
  .person-title { font-weight: 700; font-size: 15px; color: var(--navy); letter-spacing: 0.5px; margin-top: 2px; }

  .contact-list { list-style: none; margin-top: 18px; font-size: 13.5px; color: var(--ink); line-height: 21px; }
  .contact-list li { display: flex; align-items: flex-start; }
  .contact-list .icon { width: 14px; height: 14px; margin: 3px 8px 0 0; flex: none; fill: var(--navy); }
  .contact-list .indent { padding-left: 22px; }

  .back-square {
    position: absolute; right: 56px; top: 118px;
    width: 64px; height: 64px; background: var(--navy);
  }
</style>
</head>
<body>
  <section class="card card-front" aria-label="Card front">
    <div class="front-brand">
      <div class="brand-square"></div>
      <div class="brand-name">Quillvane Lawyers</div>
    </div>
  </section>

  <section class="card card-back" aria-label="Card back">
    <div class="back-brand">Quillvane Lawyers</div>

    <div class="person">
      <h1 class="person-name">PAUL WEXBURY</h1>
      <p class="person-title">MANAGING PARTNER</p>
      <ul class="contact-list">
        <li><svg class="icon" viewBox="0 0 14 14"><path d="M7 0a4.6 4.6 0 0 0-4.6 4.6C2.4 8 7 14 7 14s4.6-6 4.6-9.4A4.6 4.6 0 0 0 7 0zm0 6.4a1.8 1.8 0 1 1 0-3.6 1.8 1.8 0 0 1 0 3.6z"/></svg>Level 9, 41 Tansy Lane</li>
        <li class="indent">Sydney NSW 2000</li>
        <li><svg class="icon" viewBox="0 0 14 14"><path d="M1 4.5C1 2.5 4 1.5 7 1.5s6 1 6 3v1.5H9.6V4.6H4.4V6H1zM3 7h8l2 5H1z"/></svg>02 7346 2190 (Main)</li>
        <li><svg class="icon" viewBox="0 0 14 14"><path d="M1 4.5C1 2.5 4 1.5 7 1.5s6 1 6 3v1.5H9.6V4.6H4.4V6H1zM3 7h8l2 5H1z"/></svg>02 6273 4415 (Direct)</li>
        <li><svg class="icon" viewBox="0 0 14 14"><path d="M0 2.5h14v1L7 8 0 3.5zM0 5l7 4.5L14 5v6.5H0z"/></svg>paul@qvlegal.com.au</li>
        <li><svg class="icon" viewBox="0 0 14 14"><circle cx="7" cy="7" r="6" fill="none" stroke="#1f2466" stroke-width="1.3"/><path d="M1 6.4h12v1.2H1z"/><ellipse cx="7" cy="7" rx="2.6" ry="6" fill="none" stroke="#1f2466" stroke-width="1.1"/></svg>www.qvlegal.com.au</li>
      </ul>
    </div>

    <div class="back-square"></div>
  </section>
</body>
</html>
```